Fresh Produce Outlet needs a Poster Design

Hi,
We are Brightleaf Harvest Market, a fruit and veg outlet based in the suburb of Yanchep, Perth, Western Australia.Apart from fresh produce, we also stock nuts and grains, organic products and specialty grocery. We are about to launch a re-branding exercise, projecting ourselves as 'the' shop for fresh produce; quality, taste and freshness being our key differentiators. We are competing against a big supermarket chain who are using marketing muscle power to shut us down and we want to respond with a series of posters which are simple yet bold and sends a clear and positive message to our customers about what we have to offer.
Please feel free to visit our Facebook page www.facebook.com/brightleafharvestmkt to get an idea about our current branding,logo and the shop in general.
Regards
Team - Brightleaf Harvest Market
Target Market(s)
Residents of Yanchep and surrounding suburbs
Industry/Entity Type
Retail
Look and feel

```html
<!DOCTYPE html>
<html lang="en">
<head>
<meta charset="utf-8">
<title>Brightleaf Harvest Market – Poster</title>
<link rel="stylesheet" href="https://fonts.googleapis.com/css2?family=Quicksand:wght@400;500;700&family=Fredoka:wght@600&family=Kalam:wght@400;700&family=Open+Sans:wght@600;700&display=swap">
<style>
  :root {
    --bg-top: #f4f7ef;
    --bg-bottom: #e9f0e0;
    --orange: #f47a0c;
    --leaf: #3d5c12;
    --olive-text: #4b5a2c;
    --grey-text: #5e5e5e;
    --body-text: #3f3f3f;
    --white: #ffffff;
    --juice-green: #5f9a1f;
    --juice-red: #e1271f;
    --juice-orange: #f77a10;
  }
  * { margin: 0; padding: 0; box-sizing: border-box; }
  html, body { width: 849px; height: 1200px; overflow: hidden; }
  body { background: var(--white); }
  .poster {
    position: relative;
    width: 849px;
    height: 1200px;
    overflow: hidden;
    background: linear-gradient(180deg, var(--bg-top), var(--bg-bottom));
  }
  .hero-photo {
    position: absolute;
    left: 14px; top: 12px;
    width: 822px; height: 476px;
    background:
      linear-gradient(180deg, rgba(255,255,255,0.95) 0%, rgba(255,255,255,0) 26%, rgba(255,255,255,0) 84%, rgba(255,255,255,0.9) 100%),
      linear-gradient(90deg,
        #ffffff 0%, #ffffff 14%,
        var(--juice-green) 16%, #4f8a16 34%,
        #ffffff 37%, #ffffff 39%,
        var(--juice-red) 41%, #c91d17 60%,
        #ffffff 63%, #ffffff 65%,
        var(--juice-orange) 67%, #f58c24 86%,
        #ffffff 89%, #ffffff 100%);
  }
  .tagline-band {
    position: absolute;
    left: 14px; top: 238px;
    width: 822px; height: 52px;
    background: rgba(255,255,255,0.92);
  }
  .tagline {
    position: absolute;
    left: 0; top: 234px; width: 849px;
    text-align: center;
    font-family: "Quicksand", sans-serif;
    font-weight: 500;
    font-size: 41px;
    color: var(--olive-text);
  }
  .tagline strong { font-family: "Kalam", cursive; font-weight: 700; font-size: 44px; }
  .banner { position: absolute; left: 0; top: 0; width: 849px; height: 1200px; }
  .brand-name {
    position: absolute;
    left: 0; top: 482px; width: 849px;
    text-align: center;
    font-family: "Fredoka", sans-serif;
    font-weight: 600;
    font-size: 64px;
    color: var(--leaf);
    transform: rotate(-10.5deg);
    text-shadow: 0 0 6px var(--white), 0 0 10px var(--white), 0 0 14px var(--white);
    white-space: nowrap;
  }
  .headline {
    position: absolute;
    left: 95px; top: 636px;
    font-family: "Quicksand", sans-serif;
    font-weight: 400;
    font-size: 56px;
    color: var(--grey-text);
  }
  .intro {
    position: absolute;
    left: 90px; top: 711px; width: 670px;
    text-align: center;
    font-family: "Kalam", cursive;
    font-size: 20px;
    line-height: 45px;
    color: var(--body-text);
  }
  .location {
    position: absolute;
    left: 0; top: 844px; width: 849px;
    text-align: center;
    font-family: "Kalam", cursive;
    font-weight: 700;
    font-size: 32px;
    color: var(--body-text);
  }
  .address {
    position: absolute;
    left: 0; top: 908px; width: 849px;
    text-align: center;
    font-family: "Open Sans", sans-serif;
    font-weight: 600;
    font-size: 22px;
    color: var(--orange);
  }
  .footer-curve { position: absolute; left: 0; top: 1030px; width: 849px; height: 170px; }
  .produce-art {
    position: absolute;
    left: 34px; top: 940px;
    width: 320px; height: 152px;
    border-radius: 50%;
    background: radial-gradient(ellipse at 50% 50%, #f3a531 0%, #7fae2c 40%, #d93a24 68%, rgba(217,58,36,0) 72%);
  }
  .contact {
    position: absolute;
    left: 255px; top: 1076px; width: 380px;
    text-align: center;
    font-family: "Open Sans", sans-serif;
    color: var(--white);
  }
  .contact .phone { font-weight: 700; font-size: 36px; letter-spacing: 1px; line-height: 46px; }
  .contact .line { font-weight: 600; font-size: 21px; line-height: 30px; }
</style>
</head>
<body>
<div class="poster">
  <div class="hero-photo" role="img" aria-label="Photo of green, red and orange vegetable juices in glasses with cucumber, tomato and carrot slices"></div>
  <div class="tagline-band"></div>
  <p class="tagline">the shop for fresh produce in <strong>Yanchep</strong></p>

  <svg class="banner" viewBox="0 0 849 1200" aria-hidden="true">
    <polygon points="0,572 849,420 849,512 0,664" fill="var(--orange)"/>
  </svg>
  <h1 class="brand-name">Brightleaf Harvest Market</h1>

  <h2 class="headline">quality, taste and freshness</h2>
  <p class="intro">Yanchep, We are your local green grocer bringing you the very best and hand picked produce. We have a wide range of veggies and fruits for you along with dairy products and groceries from across the world. Do come along and visit us</p>
  <p class="location">at Yanchep Market Square !!</p>
  <p class="address">Brightleaf Harvest Market, Marlin Rd, Yanchep WA 6035, Australia</p>

  <svg class="footer-curve" viewBox="0 0 849 170" aria-hidden="true">
    <path d="M0,75 C200,10 560,-5 849,60 L849,170 L0,170 Z" fill="var(--orange)"/>
  </svg>
  <div class="produce-art" role="img" aria-label="Illustration of a pile of fresh fruit and vegetables with a glass of juice"></div>

  <div class="contact">
    <p class="phone">0895550142</p>
    <p class="line">hello@brightleafharvest.com.au</p>
    <p class="line">www.brightleafharvest.com.au/</p>
  </div>
</div>
</body>
</html>
```